Stationary - Business Card/Letterhead and envelope design

Details for my new Stationery Design Project will be added soon. , I have two logos I am trying to decide on. I will upload the eps logos shortly. I have attached a file of what i have so far. I need urgently Business cards, but also will need a letterhead template and envelopes.

PLEASE NOTE THE DEADLINE SAYS 2 DAYS but I need business card design in LESS THAN A DAY.

thanks, Details for my new Stationery Design Project will be added soon. , I have two logos I am trying to decide on. I will upload the eps logos shortly. I have attached a file of what i have so far. I need urgently Business cards, but also will need a letterhead template and envelopes.

thanks
Updates

I have uploaded one of the logos you can work with. hopefully the other one comes soon.

details for the business card.

Marnet Dobson

Managing Director

P&K Ventures Ltd

Bda: 1-441-555-0182

Email: marnet@pkvnbda.example

web: www.pkvnbda.example

Industry/Entity Type

Business

```html
<!DOCTYPE html>
<html lang="en">
<head>
<meta charset="utf-8">
<title>P&amp;K Ventures – Business Cards</title>
<link rel="stylesheet" href="https://fonts.googleapis.com/css2?family=Arimo:wght@400;700&family=Tinos:wght@700&display=swap">
<style>
  :root {
    --backdrop: #b3b3b3;
    --card-white: #ffffff;
    --teal: #17b4c8;
    --brown: #7b6a56;
    --ink: #111111;
    --url-ink: #ffffff;
    --logo-ink: #17b4c8;
  }
  * { box-sizing: border-box; margin: 0; padding: 0; }
  html, body {
    width: 1200px;
    height: 1076px;
    overflow: hidden;
    background: var(--backdrop);
  }
  .canvas {
    position: relative;
    width: 1200px;
    height: 1076px;
  }
  .card {
    position: absolute;
    left: 300px;
    width: 600px;
    height: 400px;
    border-radius: 14px;
    overflow: hidden;
    background: var(--card-white);
  }
  .card--light { top: 100px; }
  .card--teal { top: 576px; background: var(--teal); }
  .card__bands {
    position: absolute;
    inset: 0;
    width: 600px;
    height: 400px;
  }
  .card__logo {
    position: absolute;
    left: 26px;
    top: 34px;
    font-family: "Tinos", "Times New Roman", serif;
    font-weight: 700;
    font-size: 36px;
    line-height: 1;
    white-space: nowrap;
    color: var(--logo-ink);
  }
  .card--teal .card__logo {
    left: 14px;
    top: 16px;
    width: 262px;
    height: 100px;
    display: flex;
    align-items: center;
    justify-content: center;
    font-size: 34px;
    background: var(--card-white);
  }
  .card__contact {
    position: absolute;
    right: 24px;
    top: 66px;
    font-family: "Arimo", Arial, sans-serif;
    font-weight: 700;
    font-size: 14px;
    line-height: 21px;
    white-space: nowrap;
    color: var(--ink);
  }
  .card--teal .card__contact { top: 60px; }
  .card__name {
    position: absolute;
    left: 34px;
    top: 190px;
    font-family: "Tinos", "Times New Roman", serif;
    font-weight: 700;
    font-size: 66px;
    line-height: 1;
    letter-spacing: -1px;
    white-space: nowrap;
    color: var(--ink);
  }
  .card__role {
    position: absolute;
    left: 38px;
    top: 262px;
    font-family: "Arimo", Arial, sans-serif;
    font-size: 22px;
    white-space: nowrap;
    color: var(--ink);
  }
  .card--teal .card__name { left: 28px; top: 176px; }
  .card--teal .card__role { left: 34px; top: 248px; }
  .card__url {
    position: absolute;
    right: 26px;
    bottom: 36px;
    font-family: "Arimo", Arial, sans-serif;
    font-weight: 700;
    font-size: 13px;
    white-space: nowrap;
    color: var(--url-ink);
  }
  .card--teal .card__url { bottom: 22px; }
</style>
</head>
<body>
<main class="canvas">

  <section class="card card--light" aria-label="Business card, white version">
    <svg class="card__bands" viewBox="0 0 600 400" aria-hidden="true">
      <path d="M0 338 Q 320 318 600 200 L600 400 L0 400 Z" fill="var(--teal)"/>
      <path d="M0 352 Q 300 336 600 300 L600 400 L0 400 Z" fill="var(--brown)"/>
    </svg>
    <div class="card__logo">P&amp;K Ventures</div>
    <div class="card__contact">
      <p>P&amp;K Ventures Ltd</p>
      <p>BDA: 1-441-555-0182</p>
      <p>Email: marnet@pkvnbda.example</p>
    </div>
    <h1 class="card__name">Marnet Dobson</h1>
    <p class="card__role">Managing Director</p>
    <p class="card__url">www.pkvnbda.example</p>
  </section>

  <section class="card card--teal" aria-label="Business card, teal version">
    <svg class="card__bands" viewBox="0 0 600 400" aria-hidden="true">
      <path d="M0 356 L600 340 L600 400 L0 400 Z" fill="var(--brown)"/>
    </svg>
    <div class="card__logo">P&amp;K Ventures</div>
    <div class="card__contact">
      <p>P&amp;K Ventures Ltd</p>
      <p>BDA: 1-441-555-0182</p>
      <p>Email: marnet@pkvnbda.example</p>
    </div>
    <h2 class="card__name">Marnet Dobson</h2>
    <p class="card__role">Managing Director</p>
    <p class="card__url">www.pkvnbda.example</p>
  </section>

</main>
</body>
</html>
```